Lakeshore Youngsters Circle Business Card Project

We are a Minneapolis based discount club that caters to families with children. We need a business card that can be used to communicate our contact information to other businesses that may wish to offer discounts on our website.

Please use placeholders for contact information (i.e. John Doe, 123 Any Street, Any Town, etc.) and include spaces for the following: Full name, title, email, phone number, website, one line street address, city, state, and zip code.
Updates

Reason: I have extended the deadline because I had not intended the project to close so quickly.

Target Market(s)

Most of the time the business cards will be used in business to business situations. However, from time to time they may be distributed to our end customer, families with children.

Industry/Entity Type

Club

Font styles to use
Serif
Sans Serif
Other font styles liked:
• Open to suggestions

Requirements
Nice to have
• We might use the reverse side of the card as the design for our membership card.

```html
<!DOCTYPE html>
<html lang="en">
<head>
<meta charset="utf-8">
<title>Lakeshore Youngsters Circle – Business Card</title>
<link rel="stylesheet" href="https://fonts.googleapis.com/css2?family=Baloo+2:wght@500;700;800&family=Roboto+Condensed:wght@700&display=swap">
<style>
  :root {
    --stage: #e9e6e1;
    --green-light: #1cc98a;
    --green-mid: #0f9f63;
    --green-deep: #087a45;
    --edge: #06693b;
    --white: #ffffff;
    --yellow: #f2e21b;
    --orange: #f5a31a;
    --pink: #f29bc4;
    --art-orange: #f7941d;
    --art-red: #d9483b;
    --art-lime: #9bd136;
    --ghost: rgba(190, 235, 120, 0.35);
  }
  * { box-sizing: border-box; margin: 0; padding: 0; }
  html, body {
    width: 1200px; height: 913px; overflow: hidden;
    background: var(--stage);
  }
  .stage {
    position: relative; width: 1200px; height: 913px;
  }
  .card {
    position: absolute;
    width: 525px; height: 300px;
    border-radius: 6px;
    background: linear-gradient(160deg, var(--green-light) 0%, var(--green-mid) 45%, var(--green-deep) 100%);
    box-shadow: 0 4px 0 var(--edge), 0 14px 30px rgba(0,0,0,0.18);
    overflow: hidden;
    font-family: "Baloo 2", system-ui, sans-serif;
    color: var(--white);
  }
  .card--front { left: 50px; top: 306px; }
  .card--back  { left: 625px; top: 306px; }

  /* front */
  .front-mark {
    position: absolute; left: 0; right: 0; top: 40px;
    display: flex; flex-direction: column; align-items: center;
  }
  .front-art {
    width: 230px; height: 90px; border-radius: 45px;
    background: radial-gradient(ellipse at center, var(--art-orange) 0%, var(--art-red) 55%, rgba(155,209,54,0.6) 100%);
    opacity: 0.85;
  }
  .front-name {
    margin-top: 10px;
    font-weight: 800; font-size: 34px; line-height: 1;
    color: var(--white);
    text-align: center;
  }
  .front-domain {
    margin-top: 4px; font-weight: 500; font-size: 14px; color: var(--white); opacity: .85;
  }
  .tagline {
    position: absolute; left: 0; right: 0; bottom: 34px;
    text-align: center;
    font-family: "Roboto Condensed", Arial, sans-serif;
    font-weight: 700; font-size: 22px; letter-spacing: .3px;
    text-transform: uppercase;
  }

  /* back */
  .ghost-name {
    position: absolute; right: 22px; top: 68px; width: 250px;
    font-weight: 800; font-size: 42px; line-height: .95;
    color: var(--ghost); text-align: right;
  }
  .back-art {
    position: absolute; right: 40px; bottom: 28px;
    width: 150px; height: 56px; border-radius: 28px;
    background: radial-gradient(ellipse at center, rgba(155,209,54,0.35), rgba(155,209,54,0));
  }
  .back-mark {
    position: absolute; left: 26px; top: 26px;
    display: flex; align-items: center; gap: 8px;
  }
  .back-mark__dot {
    width: 22px; height: 22px; border-radius: 50%; background: var(--orange);
  }
  .back-mark__name {
    font-weight: 800; font-size: 17px; line-height: 1; color: var(--white);
  }
  .person { position: absolute; left: 26px; top: 100px; }
  .person__name { font-weight: 800; font-size: 40px; line-height: 1; color: var(--yellow); }
  .person__title { font-weight: 700; font-size: 19px; line-height: 1.1; color: var(--yellow); }
  .contact {
    position: absolute; left: 26px; top: 178px;
    list-style: none; display: flex; flex-direction: column; gap: 6px;
    font-weight: 500; font-size: 16px; line-height: 1.15; color: var(--orange);
  }
  .contact li { display: flex; align-items: flex-start; gap: 10px; }
  .contact svg { flex: none; width: 18px; height: 18px; margin-top: 1px; }
  .contact .email { color: var(--pink); }
</style>
</head>
<body>
<main class="stage">

  <section class="card card--front" aria-label="Card front">
    <div class="front-mark">
      <div class="front-art" role="img" aria-label="Colourful painted handprints and a cartoon mascot behind the club name"></div>
      <div class="front-name">Lakeshore Youngsters Circle</div>
      <div class="front-domain">lakeshoreyc.com</div>
    </div>
    <p class="tagline">Make your child a member today!</p>
  </section>

  <section class="card card--back" aria-label="Card back">
    <div class="ghost-name" aria-hidden="true">Lakeshore Youngsters Circle</div>
    <div class="back-art" role="img" aria-label="Faint handprints and mascot decoration"></div>

    <div class="back-mark">
      <span class="back-mark__dot"></span>
      <span class="back-mark__name">Lakeshore Youngsters Circle</span>
    </div>

    <div class="person">
      <div class="person__name">John Doe</div>
      <div class="person__title">Graphic Designer</div>
    </div>

    <ul class="contact">
      <li>
        <svg viewBox="0 0 18 18" aria-hidden="true"><rect x="4" y="1.5" width="10" height="15" rx="1.5" fill="none" stroke="var(--orange)" stroke-width="1.6"/><line x1="7.5" y1="13.5" x2="10.5" y2="13.5" stroke="var(--orange)" stroke-width="1.4"/></svg>
        <span>+1 612 555 - 0147</span>
      </li>
      <li>
        <svg viewBox="0 0 18 18" aria-hidden="true"><path d="M9 17s-6-6.2-6-10a6 6 0 0 1 12 0c0 3.8-6 10-6 10z" fill="var(--orange)"/><circle cx="9" cy="7" r="2.2" fill="var(--green-mid)"/></svg>
        <span>123 Any Street, Suite 4<br>Any Town, MN 55401</span>
      </li>
      <li class="email">
        <svg viewBox="0 0 18 18" aria-hidden="true"><rect x="1.5" y="4" width="15" height="10" rx="1" fill="var(--pink)"/><path d="M1.5 4.5 9 10l7.5-5.5" fill="none" stroke="var(--green-mid)" stroke-width="1.2"/></svg>
        <span>john.doe@lakeshoreyc.com</span>
      </li>
    </ul>
  </section>

</main>
</body>
</html>
```